Wine Label Design

A wine label for 750ml bottles. Same label for different varieties with the variety / region / vintage to be updated as required.
Brand: Beyond the Ridge
Product Use: Front and Back label suitable for a 750 ml bottle (preferably Burgundy bottles)
Design Brief: Beyond the Ridge is a small winery that produces limited amounts of hand crafted wines that are aimed at the mid to top end of the market and requires a label befitting the work that goes into the creation of the wine. In terms of style i don't have any preconceptions and am open to a broad range of design suggestions at the same level of existing premium brands or innovative brands.
Must Have for Front label
Front Label
Beyond the Ridge
2013
Grampians
Shiraz
750ML (should be in smaller text)
Alc. 14% by Vol. (should be in smaller text)
Must Have for Back Label
Beyond the Ridge
2013
Grampians
Shiraz
www.beyondtheridge.com.au (should be in smaller text)
Product of Australia
Alc.14% by Vol. (should be in smaller text)
Contains preservative 220(should be in smaller text)
Below are some guides for dimensions:
The Front Label Size can be between
100 - 120 mm (Width) x 70 - 85 mm (Height)
The back label size can be between
90 mm (Width) x 70 - 85 mm (Height)
Updates
Target Market(s)
Medium to top end of the wine market who require the label to be a reflection of the wine.
Industry/Entity Type
Product
Colors
Designer to choose colors to be used in the design.
Look and feel
Each slider illustrates characteristics of the customer's brand and the style your logo design should communicate.

```html
<!DOCTYPE html>
<html lang="en">
<head>
<meta charset="UTF-8">
<title>Beyond the Ridge – Grampians Shiraz Front Label</title>
<link rel="stylesheet" href="https://fonts.googleapis.com/css2?family=Stardos+Stencil:wght@700&family=Oswald:wght@400&display=swap">
<style>
  :root {
    --paper: #dccdb4;
    --bronze: #a88c64;
    --bronze-light: #b89d74;
    --bronze-dark: #8e7350;
    --ink: #111111;
    --shade: #3b2d1c;
  }
  html, body {
    margin: 0;
    padding: 0;
    width: 1200px;
    height: 850px;
    overflow: hidden;
    background: var(--paper);
  }
  .label {
    position: relative;
    width: 1200px;
    height: 850px;
    background: var(--paper);
  }
  .frame-outer {
    position: absolute;
    left: 211px; top: 61px;
    width: 793px; height: 702px;
    border: 3px solid var(--bronze);
  }
  .frame-inner {
    position: absolute;
    left: 241px; top: 86px;
    width: 730px; height: 649px;
    border: 3px solid var(--ink);
  }
  .ornament {
    position: absolute;
    width: 12px; height: 12px;
    border-radius: 50%;
  }
  .ornament--dark { background: var(--ink); }
  .ornament--light { background: var(--bronze); }
  .engraved {
    margin: 0;
    position: absolute;
    left: 0; width: 1200px;
    text-align: center;
    font-family: "Stardos Stencil", serif;
    font-weight: 700;
    color: var(--bronze);
    text-shadow: 2px 2px 0 var(--shade), -1px -1px 0 #efe4d2;
    line-height: 1;
    text-transform: uppercase;
  }
  .brand-name {
    top: 120px;
    left: 0;
    width: 1184px;
    font-size: 60px;
    letter-spacing: 1px;
  }
  .vineyard-scene {
    position: absolute;
    left: 382px; top: 236px;
  }
  .region  { top: 532px; font-size: 42px; letter-spacing: 2px; }
  .variety { top: 599px; font-size: 42px; letter-spacing: 2px; }
  .vintage { top: 662px; font-size: 42px; letter-spacing: 2px; }
  .fine-print {
    position: absolute;
    top: 769px;
    margin: 0;
    font-family: "Oswald", sans-serif;
    font-weight: 400;
    font-size: 20px;
    color: var(--ink);
    letter-spacing: 0;
    transform: scaleX(0.85);
  }
  .volume  { left: 211px; transform-origin: left center; }
  .alcohol { right: 188px; transform-origin: right center; }
</style>
</head>
<body>
<div class="label">
  <div class="frame-outer"></div>
  <div class="frame-inner"></div>

  <span class="ornament ornament--dark"  role="img" aria-label="Leaf ornament" style="left:573px;top:69px;"></span>
  <span class="ornament ornament--light" role="img" aria-label="Leaf ornament" style="left:613px;top:69px;"></span>
  <span class="ornament ornament--dark"  role="img" aria-label="Leaf ornament" style="left:573px;top:745px;"></span>
  <span class="ornament ornament--light" role="img" aria-label="Leaf ornament" style="left:613px;top:745px;"></span>
  <span class="ornament ornament--light" role="img" aria-label="Leaf ornament" style="left:220px;top:382px;"></span>
  <span class="ornament ornament--dark"  role="img" aria-label="Leaf ornament" style="left:220px;top:426px;"></span>
  <span class="ornament ornament--light" role="img" aria-label="Leaf ornament" style="left:985px;top:384px;"></span>
  <span class="ornament ornament--dark"  role="img" aria-label="Leaf ornament" style="left:985px;top:423px;"></span>

  <h1 class="engraved brand-name">Beyond the Ridge</h1>

  <svg class="vineyard-scene" width="424" height="240" viewBox="0 0 424 240" role="img" aria-label="Embossed oval illustration of hillside vineyard rows with a farmhouse, cypress trees and a fence">
    <defs>
      <linearGradient id="oval-fill" x1="0" y1="0" x2="1" y2="1">
        <stop offset="0" stop-color="var(--bronze-light)"/>
        <stop offset="1" stop-color="var(--bronze-dark)"/>
      </linearGradient>
    </defs>
    <ellipse cx="214" cy="122" rx="209" ry="116" fill="var(--ink)"/>
    <ellipse cx="209" cy="117" rx="209" ry="116" fill="url(#oval-fill)"/>
  </svg>

  <h2 class="engraved region">Grampians</h2>
  <h2 class="engraved variety">Shiraz</h2>
  <p class="engraved vintage">2013</p>

  <p class="fine-print volume">750ML</p>
  <p class="fine-print alcohol">ALC. 14% BY VOL.</p>
</div>
</body>
</html>
```